riverstonelightcare - healing business promotion

I have and energy / intuitive healing and kinesiology business. working with people who are looking for healing outside of the modern medical model, who have tried but failed in their search for understanding their conditions and why health and or happiness eludes them. the healing is done with love, patience and understanding. I am looking to be taken seriously with my presentation and to reach a person who may be deterred by the thought of angels and intuition! but to not exclude those that are attracted to that also.

Industry/Entity Type

Medical

Contact Information for Business Card

riverstonelightcare
calm clear gentle energy renewal method
tamsin corrine hale
energy healing / kinesiology and neurotraining
0417362815 07 4186 2751
home visits available for cairns and tablelands
t.chale@maildrop-example.net

Requirements
Should not have
• Primary colours

```html
<!DOCTYPE html>
<html lang="en">
<head>
<meta charset="utf-8">
<title>riverstonelightcare – business card</title>
<link href="https://fonts.googleapis.com/css2?family=PT+Sans:ital,wght@0,400;1,400&display=swap" rel="stylesheet">
<style>
  :root {
    --backdrop: #2b2b2b;
    --leaf-green: #8fcb23;
    --card-white: #ffffff;
    --ink-dark: #3d4a2c;
    --ink-grey: #8e8e8e;
    --ink-tagline: #4a4a4a;
    --accent-teal: #6cc3bd;
    --contact-green: #8cc63f;
  }
  * { margin: 0; padding: 0; box-sizing: border-box; }
  html, body {
    width: 1200px;
    height: 900px;
    overflow: hidden;
    background: var(--backdrop);
    font-family: "PT Sans", "Trebuchet MS", sans-serif;
  }
  .canvas {
    position: relative;
    width: 1200px;
    height: 900px;
  }
  .card {
    position: absolute;
    width: 680px;
    height: 400px;
    border-radius: 34px;
    box-shadow: 0 10px 30px rgba(0, 0, 0, 0.45);
    display: flex;
    flex-direction: column;
    align-items: center;
  }
  .card-front {
    left: 50px;
    top: 45px;
    background: var(--leaf-green);
    justify-content: center;
    gap: 34px;
  }
  .card-back {
    left: 470px;
    top: 455px;
    background: var(--card-white);
    padding-top: 52px;
  }
  .brand-dot {
    width: 96px;
    height: 96px;
    border-radius: 50%;
  }
  .card-front .brand-dot { background: var(--card-white); }
  .card-back .brand-dot { background: var(--accent-teal); width: 78px; height: 78px; }
  .brand-name {
    font-weight: 400;
    letter-spacing: 0.5px;
  }
  .card-front .brand-name {
    font-size: 40px;
    color: var(--ink-dark);
  }
  .card-back .brand-name {
    margin-top: 22px;
    font-size: 36px;
    color: var(--ink-grey);
    line-height: 1;
  }
  .tagline {
    margin-top: 6px;
    font-size: 19px;
    font-style: italic;
    color: var(--ink-tagline);
    letter-spacing: 0.3px;
  }
  .contact {
    margin-top: 32px;
    text-align: center;
    font-size: 14px;
    line-height: 1.3;
    color: var(--contact-green);
    letter-spacing: 0.2px;
  }
  .contact .practitioner { margin-bottom: 4px; }
</style>
</head>
<body>
  <main class="canvas">
    <section class="card card-front" aria-label="Business card front">
      <div class="brand-dot" aria-hidden="true"></div>
      <p class="brand-name">riverstonelightcare</p>
    </section>

    <section class="card card-back" aria-label="Business card back">
      <div class="brand-dot" aria-hidden="true"></div>
      <p class="brand-name">riverstonelightcare</p>
      <p class="tagline">calm clear gentle energy renewal method</p>
      <address class="contact">
        <p class="practitioner">Tamsin Corrine Hale</p>
        <p>Energy Healing / Kinesiology and Neuro training</p>
        <p>0417362815 07 4186 2751</p>
        <p>home visits available for cairns and tablelands</p>
        <p>t.chale@maildrop-example.net</p>
      </address>
    </section>
  </main>
</body>
</html>
```